vascular clinic webdesign (wordpress+neve theme+ elementor)

Create a nice webdesign for an existing website of a vascular surgery clinic. Vascular surgery is the medical specialty that treats arteries and veins. Content should not change. First landing page we can recreate content if needed, but internal pages should not change content. We currently use Neve theme (https://plumecraft.net/skins/orla/) in a Wordpress CMS, which is highly customizable, we prefer to keep using it, as it is standard in all our sites, and will be often upgraded. We also have Elementor Pro. Please visit current domain: lumeria.net.
Page is in portuguese. But you can do anything in English that I translate later, or you can use original domain content already in portuguese.
Selected design need to be coded in wordpress+neve+elementor

Minimum pages:
First Page/Landing page (https://lumeria.net/)
Contact page (https://lumeria.net/contato/)
Post/Article page
About us (https://lumeria.net/a-clinica/)
Posts Archive (https://lumeria.net/todos-artigos/)
The team (https://lumeria.net/sobre-nos-equipe-de-cirurgia-vascular-endovascular-ecografia-angiologia/)

Target Market(s)

mostly (70%) woman, 30 to 60 years

Industry/Entity Type

Health

Coding

Coded - Design and coding required

Number of Pages Required

5+ page

Font styles to use
Serif

Requirements
Should not have
• Will not change Wordpress for any other CMS
Prefer not to change theme Neve (https://plumecraft.net/skins/orla/)

```html
<!DOCTYPE html>
<html lang="en">
<head>
<meta charset="utf-8">
<title>Lumeria – Vascular Surgeon</title>
<link href="https://fonts.googleapis.com/css2?family=Lora:wght@400;500;600;700&display=swap" rel="stylesheet">
<style>
:root{
  --navy:#0d4a7a;--blue:#2f86c3;--sky:#2a9df4;--ink:#1e1e1e;--text:#555;--muted:#888;
  --maroon:#7a2b1d;--green:#2fa44f;--footer:#222;--copy:#1565a8;--light:#f2f2f2;--line:#ddd;
}
*{box-sizing:border-box;margin:0;padding:0}
html,body{width:1200px;height:4392px;overflow:hidden}
body{font-family:'Lora',serif;color:var(--ink);background:#fff;position:relative}
.abs{position:absolute}
section,header,footer{position:absolute;left:0;width:1200px}
.ph{position:absolute}
.heading{font-weight:700;text-align:center;font-size:23px;letter-spacing:.3px}
/* hero */
.hero{top:0;height:680px;background:linear-gradient(180deg,#2b3a43 0%,#1a272f 55%,#0f1a20 100%);overflow:visible}
.topbar{top:12px;left:126px;right:126px;display:flex;justify-content:space-between;color:#fff;font-size:13px}
.topbar span{margin-right:22px;display:inline-flex;align-items:center;gap:7px}
.social{display:flex;gap:12px}
.social i{width:13px;height:13px;border-radius:50%;background:var(--sky);display:block}
.nav{top:41px;left:126px;width:948px;height:61px;background:#fff;display:flex;align-items:center}
.brand{font-size:24px;font-weight:500;color:var(--navy);letter-spacing:1px;margin-left:18px;width:270px;display:flex;align-items:center;gap:8px}
.brand i{width:10px;height:10px;background:var(--navy);display:block}
.menu{display:flex;gap:24px;font-size:13px;font-weight:500;white-space:nowrap}
.menu .on{color:var(--blue);border-bottom:2px solid var(--blue)}
.appt{margin-left:auto;height:61px;width:160px;background:var(--navy);color:#fff;font-size:11px;font-weight:600;display:flex;align-items:center;justify-content:center;gap:12px;text-align:center;line-height:1.2}
.appt b{width:30px;height:30px;border-radius:50%;border:2px solid #fff;display:block}
.hero h1{position:absolute;top:282px;width:100%;text-align:center;color:var(--sky);font-size:38px;font-weight:600}
.hero .sub{position:absolute;top:332px;width:100%;text-align:center;color:#fff;font-size:16px}
.stat{position:absolute;background:#fff;text-align:center;box-shadow:0 6px 18px rgba(0,0,0,.12);padding:22px 24px}
.stat h3{color:var(--blue);font-size:15px;font-weight:600;margin-bottom:10px}
.stat p{font-size:11.5px;color:#444;line-height:1.55}
.stat.feature{background:var(--navy)}
.stat.feature h3,.stat.feature p{color:#fff}
/* about */
.about{top:680px;height:534px}
.about h2{position:absolute;left:126px;top:150px;font-size:24px;font-weight:700}
.about .body{position:absolute;left:126px;top:220px;width:390px;font-size:12px;line-height:1.6;color:#444}
.about .lead{color:var(--navy);font-weight:600;font-size:15px;margin:22px 0 8px;line-height:1.45}
.btn-out{position:absolute;left:126px;top:442px;width:110px;height:32px;border:1.5px solid var(--ink);border-radius:4px;font-size:10.5px;font-weight:600;display:flex;align-items:center;justify-content:center}
/* specialties */
.spec{top:1214px;height:486px;background:var(--blue)}
.spec .heading{color:#fff;padding-top:64px}
.card{position:absolute;top:141px;width:217px;height:253px;background:linear-gradient(160deg,#cfa58f,#e5c6b2);border:2px solid #fff}
.card .lab{position:absolute;left:14px;right:14px;bottom:-6px;background:#fff;text-align:center;padding:10px 0 8px;font-size:13.5px;box-shadow:0 3px 10px rgba(0,0,0,.1)}
.card .lab small{display:block;color:var(--blue);font-size:10.5px;margin-top:4px}
.arrow{position:absolute;top:250px;width:22px;height:22px;border-radius:50%;background:rgba(255,255,255,.45);display:flex;align-items:center;justify-content:center}
/* specialist */
.specialist{top:1700px;height:440px}
.specialist h2{position:absolute;left:611px;top:66px;font-size:24px;line-height:1.1;color:var(--navy);font-weight:700}
.acc{position:absolute;left:611px;width:464px;display:flex;align-items:center;font-size:15px;font-weight:600;white-space:nowrap}
.acc .rule{flex:1;height:1px;background:#999;margin:0 0 0 14px}
.acc .ic{width:20px;height:20px;border-radius:50%;border:1.5px solid #333;display:flex;align-items:center;justify-content:center;font-size:14px;font-weight:400;margin-left:4px}
.acc-txt{position:absolute;left:611px;top:205px;width:420px;font-size:12px;line-height:1.55;color:#666}
.arterial{top:2140px;height:216px;background:var(--maroon)}
.arterial h2{position:absolute;left:301px;top:66px;color:#fff;font-size:24px;font-weight:700}
.arterial p{position:absolute;left:301px;top:112px;color:#fff;font-size:13px;line-height:1.5;width:360px}
/* cta */
.cta{top:2419px;left:126px;width:948px;height:152px;border:1px solid var(--line);border-radius:4px}
.cta h3{position:absolute;left:40px;top:36px;width:540px;text-align:center;font-size:21px;font-weight:600;line-height:1.2}
.cta p{position:absolute;left:40px;top:104px;width:540px;text-align:center;font-size:12.5px;color:#444}
.wa{position:absolute;left:660px;top:40px;width:264px;height:75px;background:var(--green);color:#fff;font-size:17px;font-weight:500;display:flex;align-items:center;justify-content:center;gap:10px;border-radius:2px}
/* team */
.team{top:2641px;height:527px;background:var(--light)}
.team .heading{padding-top:64px}
.viewall{position:absolute;right:126px;font-size:12.5px;color:#333}
.member{position:absolute;top:150px;width:217px;text-align:center}
.member .ph{position:relative;height:252px;background:linear-gradient(180deg,#e9e9e9,#bfc3c6);border:1px solid #ddd}
.member h4{color:var(--blue);font-size:14px;font-weight:600;margin-top:14px}
.member small{display:block;font-size:11.5px;color:#444;line-height:1.4}
/* articles */
.articles{top:3168px;height:515px}
.articles .heading{padding-top:64px}
.post{position:absolute;top:145px;width:299px;text-align:center}
.post .ph{position:relative;height:194px;background:linear-gradient(180deg,#f3ece6,#c9a28a)}
.post .date{position:absolute;left:80px;top:0;background:var(--navy);color:#fff;font-size:12px;padding:6px 20px}
.post h4{font-size:15px;font-weight:600;margin-top:24px}
.post p{font-size:12px;color:#888;line-height:1.55;margin-top:10px;padding:0 14px}
.post a{display:block;color:var(--blue);font-size:12px;margin-top:8px;text-decoration:none}
/* schedule */
.schedule{top:3683px;height:472px}
.sched-l{position:absolute;left:0;top:0;width:610px;height:472px;background:var(--navy)}
.sched-l .heading{color:#fff;padding-top:56px}
.field{position:absolute;left:162px;width:356px;height:36px;background:#fff;font-size:11px;color:#888;display:flex;align-items:center;padding-left:12px;gap:10px}
.submit{position:absolute;left:288px;top:392px;width:104px;height:34px;border:1.5px solid #fff;color:#fff;font-size:11px;font-weight:600;display:flex;align-items:center;justify-content:center}
.map{position:absolute;left:610px;top:0;width:590px;height:472px;background:linear-gradient(135deg,#eef1ed,#e4e8e3)}
/* footer */
.site-footer{top:4155px;height:210px;background:var(--footer);color:#fff}
.fnav{position:absolute;top:24px;width:100%;display:flex;justify-content:center;gap:30px;font-size:13px}
.fnav .on{color:var(--blue)}
.flogo{position:absolute;left:126px;top:108px;font-size:30px;letter-spacing:1px;font-weight:500}
.fcol{position:absolute;top:100px;font-size:12px;line-height:1.6}
.fcol h5{color:var(--blue);font-size:11px;font-weight:500}
.fsoc{position:absolute;left:966px;top:99px;display:grid;grid-template-columns:repeat(3,26px);gap:10px}
.fsoc i{width:26px;height:26px;border:1.5px solid #fff;border-radius:50%;display:block}
.copy{top:4365px;height:27px;background:var(--copy);color:#fff;font-size:12px;text-align:center;line-height:27px}
</style>
</head>
<body>

<header class="hero">
  <div class="abs topbar">
    <div><span>✉ consulta@lumeria.net</span><span>
      <svg width="12" height="12" viewBox="0 0 24 24"><path fill="#fff" d="M6.6 10.8a15 15 0 0 0 6.6 6.6l2.2-2.2c.3-.3.7-.4 1-.2 1.1.4 2.3.6 3.6.6.6 0 1 .4 1 1V20c0 .6-.4 1-1 1A17 17 0 0 1 3 4c0-.6.4-1 1-1h3.5c.6 0 1 .4 1 1 0 1.3.2 2.5.6 3.6.1.3 0 .7-.2 1z"/></svg>(011) 4000-1234</span></div>
    <div class="social"><i></i><i></i><i></i><i></i><i></i></div>
  </div>
  <nav class="abs nav">
    <div class="brand"><i></i>LUMERIA</div>
    <div class="menu"><span class="on">Home</span><span>About Us</span><span>Artical</span><span>Posts Archive</span><span>The Team</span><span>Contact</span></div>
    <div class="appt"><b></b>MAKE<br>APPOINTMENT</div>
  </nav>
  <div class="ph" role="img" aria-label="Surgeons operating in a dimmed operating room" style="left:0;right:0;top:102px;height:480px;background:radial-gradient(ellipse at 50% 40%,rgba(70,90,100,.35),transparent 70%)"></div>
  <h1>Vascular Surgeon</h1>
  <div class="sub">Vascular Surgeon in São Paulo</div>
  <svg class="abs" style="left:0;top:560px" width="1200" height="120" viewBox="0 0 1200 120">
    <path d="M0 98 Q600 -10 1200 98 L1200 120 L0 120Z" fill="#1d6aa8"/>
    <path d="M0 112 Q600 8 1200 112 L1200 120 L0 120Z" fill="#fff"/>
  </svg>
  <div class="stat" style="left:150px;top:583px;width:281px;min-height:119px"><h3>35 YEARS</h3><p>We have been treating vascular diseases for 35 years ...</p></div>
  <div class="stat feature" style="left:457px;top:568px;width:285px;padding:16px 24px"><h3>4 GENERATIONS</h3><p>There are 4 generations of vascular in the family. Knowledge that has passed through generations and the best universities.</p></div>
  <div class="stat" style="left:765px;top:583px;width:285px;min-height:119px"><h3>+10,000 PROCEDURES</h3><p>More than 10 thousand vascular procedures performed...</p></div>
</header>

<section class="about">
  <h2>ABOUT US</h2>
  <div class="body">
    <p>The Lumeria - Advanced Institute of Medicine is a fully equipped hospital day to perform the latest procedures with minimally invasive surgery with the use of laser, radiofrequency and fluoroscopy.</p>
    <p class="lead">Almost 40 years taking care of you.<br>4 generations of doctors.</p>
    <p>Varicose veins and spider veins : laser treatment (CLaCs technique) and Annox (sedation) .</p>
  </div>
  <div class="btn-out">READ MORE</div>
  <div class="ph" role="img" aria-label="Red and white clinic building exterior" style="left:639px;top:116px;width:435px;height:370px;background:linear-gradient(180deg,#3f8fd8 0%,#c63a2c 45%,#9a9a92 100%)"></div>
  <div class="ph" role="img" aria-label="Video still of a leg treatment" style="left:585px;top:283px;width:177px;height:174px;background:linear-gradient(160deg,#cfd8e0,#7b9bb8);border:3px solid #fff"></div>
  <div class="abs" style="left:585px;top:400px;width:44px;height:54px;background:var(--navy);display:flex;align-items:center;justify-content:center"><svg width="16" height="18"><path d="M2 1 L15 9 L2 17Z" fill="#fff"/></svg></div>
</section>

<section class="spec">
  <div class="heading">SPECIALTIES</div>
  <div class="arrow" style="left:74px"><svg width="10" height="10"><path d="M8 5H2M5 2 2 5 5 8" stroke="#fff" stroke-width="1.5" fill="none"/></svg></div>
  <div class="arrow" style="left:1104px;background:#fff"><svg width="10" height="10"><path d="M2 5H8M5 2 8 5 5 8" stroke="#2f86c3" stroke-width="1.5" fill="none"/></svg></div>
  <div class="card" role="img" aria-label="Arterial surgery in progress" style="left:126px"><div class="lab">Arterial Surgery<small>› Read More</small></div></div>
  <div class="card" role="img" aria-label="Vein surgery with laser fibre" style="left:370px;background:linear-gradient(160deg,#b7c3c9,#e1c6b4)"><div class="lab">Vein Surgery<small>› Read More</small></div></div>
  <div class="card" role="img" aria-label="Lymphatic massage treatment" style="left:612px;background:linear-gradient(160deg,#e6c0a8,#c98f74)"><div class="lab">Lymphatic Treatment<small>› Read More</small></div></div>
  <div class="card" role="img" aria-label="Endovascular catheter procedure" style="left:856px;background:linear-gradient(160deg,#7fb0c4,#d8e4ea)"><div class="lab" style="bottom:22px">Endovascular surgery<small>› Read More</small></div></div>
</section>

<section class="specialist">
  <div class="ph" role="img" aria-label="Clinic building with red facade under blue sky" style="left:0;top:0;width:559px;height:440px;background:linear-gradient(180deg,#2f7fd0 0%,#c0392b 50%,#6d7a62 100%)"></div>
  <h2>SPECIALIST IN VASCULAR<br>SURGERY AND ANGIOLOGY</h2>
  <div class="acc" style="top:176px">Laser Treatment of Varicose Veins<span class="rule"></span><span class="ic">−</span></div>
  <div class="acc-txt">We do all venous treatments, from foam, laser, microsurgery, aesthetics and much more. Largest Brazilian experience in laser for varicose veins published.</div>
  <div class="acc" style="top:295px">Treatment of Lipedema<span class="rule"></span><span class="ic">+</span></div>
  <div class="acc" style="top:350px">All reimbursement agreements<span class="rule"></span><span class="ic">+</span></div>
</section>

<section class="arterial">
  <div class="ph" role="img" aria-label="Street and building base continuing from photo above" style="left:0;top:0;width:235px;height:216px;background:linear-gradient(180deg,#6d7a62,#4a4f47)"></div>
  <h2>ARTERIAL DISEASES</h2>
  <p>The vascular surgery team is used to endovascular and traditional arterial surgeries.</p>
  <div class="ph" role="img" aria-label="Red blood cells and platelets" style="left:702px;top:20px;width:372px;height:176px;border:3px solid #fff;background:radial-gradient(circle at 40% 50%,#e03a2f,#8c1510 70%)"></div>
</section>

<section class="cta">
  <h3>Aneurysm surgery, carotid stenosis, laser varicose veins and other vascular diseases</h3>
  <p>Vascular Surgeon in São Paulo, SP</p>
  <div class="wa"><svg width="24" height="24" viewBox="0 0 24 24"><circle cx="12" cy="12" r="10" stroke="#fff" stroke-width="2" fill="none"/></svg>Contact Us Now</div>
</section>

<section class="team">
  <div class="heading">THE TEAM</div>
  <div class="viewall" style="top:93px">View All →</div>
  <div class="member" style="left:126px"><div class="ph" role="img" aria-label="Portrait of a doctor in white coat"></div><h4>Prof. Dr. Henrique</h4><small>Vasconi Lemos</small></div>
  <div class="member" style="left:370px"><div class="ph" role="img" aria-label="Portrait of a doctor in dark suit" style="background:linear-gradient(180deg,#fff,#cfcfcf)"></div><h4>Prof. Dr. Otávio Reis</h4><small>Angiology</small></div>
  <div class="member" style="left:612px"><div class="ph" role="img" aria-label="Portrait of a doctor in dark suit" style="background:linear-gradient(180deg,#fff,#cfcfcf)"><span class="abs" style="left:64px;bottom:10px;width:90px;height:24px;background:var(--blue);color:#fff;font-size:12px;line-height:24px;border-radius:2px">more</span></div><h4>Prof. Dr. Caio Reis</h4><small>Neurosurgery</small></div>
  <div class="member" style="left:856px"><div class="ph" role="img" aria-label="Portrait of a doctor in white coat" style="background:linear-gradient(180deg,#6e6e6e,#9fa9b3)"></div><h4>Prof. Dr. Tomás Lacerda</h4><small>Vascular and Endovascular<br>Surgery</small></div>
</section>

<section class="articles">
  <div class="heading">ARTICAL</div>
  <div class="viewall" style="top:82px">View All →</div>
  <div class="post" style="left:126px"><div class="ph" role="img" aria-label="Legs of women standing in a row"><span class="date">January 15, 2021</span></div><h4>Lipedema: what is it?</h4><p>Have you heard of lipedema? The disease, considered chronic by specialists...</p><a>› Read More</a></div>
  <div class="post" style="left:450px"><div class="ph" role="img" aria-label="Board of Mediterranean food" style="background:linear-gradient(180deg,#6b7a4a,#8a5a38)"><span class="date">January 19, 2021</span></div><h4>How to make the Mediterranean...</h4><p>The Mediterranean diet, also known as the Mediterranean diet, is more...</p><a>› Read More</a></div>
  <div class="post" style="left:774px"><div class="ph" role="img" aria-label="Legs of women standing in a row"><span class="date">January 20, 2021</span></div><h4>Probiotics</h4><p>Probiotics are being used more and more in medicine. Probiotics are live...</p><a>› Read More</a></div>
</section>

<section class="schedule">
  <div class="sched-l">
    <div class="heading">SCHEDULE NOW!</div>
    <div class="field" style="top:122px">👤 Name</div>
    <div class="field" style="top:172px">✉ Email</div>
    <div class="field" style="top:222px">▯ Phone</div>
    <div class="field" style="top:271px;height:95px;align-items:flex-start;padding-top:11px">▢ Message</div>
    <div class="submit">SUBMIT</div>
  </div>
  <div class="map" role="img" aria-label="Street map showing the clinic location in São Paulo"></div>
</section>

<footer class="site-footer">
  <div class="fnav"><span class="on">Home</span><span>About Us</span><span>Artical</span><span>Posts Archive</span><span>The Team</span><span>Contacta</span></div>
  <div class="flogo">LUMERIA</div>
  <div class="fcol" style="left:471px"><h5>ADDRESS:</h5>Av. das Palmeiras, 1180, São Paulo,<br>SP</div>
  <div class="fcol" style="left:741px"><h5>CALL US:</h5>☎ (011) 4000-1234<br>✉ secretaria@lumeria.net</div>
  <div class="fsoc"><i></i><i></i><i></i><i></i><i></i></div>
</footer>
<div class="abs copy" style="left:0;width:1200px">Copyright © 2021 Lumeria. All Rights Reserved</div>

</body>
</html>
```